4 Page Music Brochure design

We need assistance in designing a 4 Page A4 (A3 folded) Brochure promoting International Music Tour options for school groups. We have included text in the brief as well as images to be used in the brochure.

```html
<!DOCTYPE html>
<html lang="en">
<head>
<meta charset="utf-8">
<title>Music Tours Brochure Spread</title>
<link href="https://fonts.googleapis.com/css2?family=Fira+Sans+Condensed:wght@300;500;600&family=Fira+Sans:wght@300;400&display=swap" rel="stylesheet">
<style>
  :root {
    --page-bg: #d9d9d9;
    --maroon: #6c1a1f;
    --maroon-deep: #5a1418;
    --text-light: #f1e4e4;
    --rule: #f4eaea;
  }
  * { box-sizing: border-box; margin: 0; padding: 0; }
  html, body {
    width: 1200px; height: 900px; overflow: hidden;
    background: var(--page-bg);
  }
  .spread {
    position: absolute; left: 40px; top: 43px;
    width: 1120px; height: 814px;
    display: flex;
    background: var(--maroon);
  }
  /* Left page */
  .page-left {
    width: 544px; height: 100%;
    display: flex; flex-direction: column;
    background: var(--maroon);
  }
  .hero-photo {
    height: 519px;
    background:
      linear-gradient(180deg, #9fb6d2 0%, #c9d5e2 35%, #6f6a66 60%, #4f4a46 80%, #8a8580 100%);
  }
  .feature {
    padding: 18px 18px 0 18px;
    color: var(--text-light);
  }
  .feature-title {
    font-family: "Fira Sans Condensed", sans-serif;
    font-weight: 600; font-size: 18px; line-height: 1.1;
    color: #fff;
  }
  .feature-dates {
    font-family: "Fira Sans Condensed", sans-serif;
    font-weight: 300; font-size: 17px; line-height: 1.25;
    color: #fff; margin-bottom: 10px;
  }
  .feature-body {
    width: 370px;
    font-family: "Fira Sans", sans-serif;
    font-weight: 300; font-size: 11.4px; line-height: 18.4px;
  }
  /* Right page */
  .page-right {
    flex: 1; height: 100%;
    display: flex; flex-direction: column; justify-content: space-between;
    background: var(--maroon-deep);
  }
  .tour {
    height: 192px;
    display: flex;
  }
  .tour-photo { width: 291px; height: 100%; }
  .tour-info {
    flex: 1; height: 100%;
    padding: 9px 12px 0 17px;
    background: var(--maroon);
    color: var(--text-light);
    position: relative;
  }
  .tour-info.has-rule::after {
    content: ""; position: absolute;
    left: 17px; right: 12px; bottom: 0;
    height: 2px; background: var(--rule);
  }
  .tour-title {
    font-family: "Fira Sans Condensed", sans-serif;
    font-weight: 600; font-size: 18px; line-height: 1.2;
    color: #fff; margin-bottom: 6px;
  }
  .tour-body {
    font-family: "Fira Sans", sans-serif;
    font-weight: 300; font-size: 11.2px; line-height: 18.4px;
  }
  .photo-hall { background: linear-gradient(180deg, #241408 0%, #6b3a16 55%, #c27a2a 70%, #2a180c 100%); }
  .photo-gates { background: linear-gradient(90deg, #d4361a 0%, #7a1508 35%, #3a0e08 50%, #7a1508 65%, #e0461e 100%); }
  .photo-opera { background: radial-gradient(ellipse at 40% 60%, #f0d8b0 0%, #a8622c 30%, #4a2010 75%, #24100a 100%); }
  .photo-band { background: linear-gradient(180deg, #8a7a6a 0%, #b8b0a8 30%, #b0282c 60%, #2a1c1c 100%); }
</style>
</head>
<body>
<main class="spread">
  <section class="page-left">
    <div class="hero-photo" role="img" aria-label="Gothic cathedral towers above a busy old-town street with a tram"></div>
    <article class="feature">
      <h2 class="feature-title">Global Choir Festival</h2>
      <p class="feature-dates">(5th to the 15th of July 2020)</p>
      <p class="feature-body">Join the biggest Choral Music event in the world with Choirs from over 80 different countries and regions, taking part in adjudicated performances, individual coaching, and singing workshops. Held in Belgium in the cities Antwerp and Ghent, this is a fantastic opportunity to perform on the world stage as well as take in the rich history of the Flanders region. With the option to extend your trip to include France, Germany, Italy, Austria or other nearby European Countries.</p>
    </article>
  </section>

  <section class="page-right">
    <article class="tour">
      <div class="tour-photo photo-hall" role="img" aria-label="Concert hall facade lit up at night"></div>
      <div class="tour-info has-rule">
        <h3 class="tour-title">Harmon Concert Hall</h3>
        <p class="tour-body">The once in a life time opportunity to perform on one of the world’s most famous music venues. Choirs will also have the opportunity to participate in performances, clinics, workshops, and exchanges. Based in New York City, there will also be the chance to include stops in Washington DC, Los Angeles, or San Francisco on to your trip.</p>
      </div>
    </article>
    <article class="tour">
      <div class="tour-photo photo-gates" role="img" aria-label="Path through a tunnel of red shrine gates"></div>
      <div class="tour-info has-rule">
        <h3 class="tour-title">Japan Music Tours</h3>
        <p class="tour-body">Travel to the land of the Rising Sun and take part in school exchanges, public performances and the chance to perform at iconic theme parks Tokyo Dreamland and Studio Park Japan. Students will have the opportunity to take a Japanese Cooking Class, partake in a Traditional Japanese Tea Ceremony, see a Kabuki show, and ride the bullet train.</p>
      </div>
    </article>
    <article class="tour">
      <div class="tour-photo photo-opera" role="img" aria-label="Orchestra on stage inside an ornate opera house"></div>
      <div class="tour-info has-rule">
        <h3 class="tour-title">European Instrumental Tours</h3>
        <p class="tour-body">Play in Austria, France, Germany, the United Kingdom, or wherever your heart desires, your band, orchestra or ensemble will have the opportunity to perform at concert halls across Europe. As well as opportunities to participate in festivals, public performances and workshop with music professionals.</p>
      </div>
    </article>
    <article class="tour">
      <div class="tour-photo photo-band" role="img" aria-label="Marching band in red uniforms parading down a city street"></div>
      <div class="tour-info">
        <h3 class="tour-title">US Music Road Trip</h3>
        <p class="tour-body">Trace a path across the US journeying from Jazz to Blues to Soul onto Rock’n’Roll before finishing in Country Music capital of the world – Nashville. You will visit New Orleans, Memphis and Nashville where you will have the opportunity to perform at unique venues, undertake school exchanges and participate in workshops with musicians and professionals.</p>
      </div>
    </article>
  </section>
</main>
</body>
</html>
```